Harrowgate Supply Group Business Card Design

The Business Card will be one side only with Harrowgate Supplies Group Logo
Card should have:
Name
Title
Office phone Number
Cell Number
email address
Website
Street Address
Our Slogan is Rugged and Reliable
Looking for something that stands out from other business cards

Target Market(s)

Heavy equipment Lease Company

```html
<!DOCTYPE html>
<html lang="en">
<head>
<meta charset="utf-8">
<title>Harrowgate Supplies Group – Business Card</title>
<link rel="stylesheet" href="https://fonts.googleapis.com/css2?family=Arimo:wght@400;700&display=swap">
<style>
  :root {
    --navy: #2d2f7c;
    --red: #d5202f;
    --white: #ffffff;
    --stage: #2b2b2e;
  }
  html, body {
    margin: 0;
    width: 1200px;
    height: 800px;
    overflow: hidden;
    background: var(--stage);
    font-family: "Arimo", Arial, sans-serif;
  }
  .canvas {
    position: relative;
    width: 1200px;
    height: 800px;
  }
  .card {
    position: absolute;
    top: 245px;
    width: 540px;
    height: 309px;
    overflow: hidden;
    box-shadow: 0 14px 30px rgba(0,0,0,.45);
  }
  .card-back { left: 40px; background: var(--navy); color: var(--white); }
  .card-front { left: 620px; background: var(--white); }
  .card svg.shapes { position: absolute; inset: 0; }

  /* back */
  .brand-lockup { position: absolute; left: 150px; top: 108px; display: flex; align-items: center; gap: 14px; }
  .brand-mark { width: 44px; height: 44px; border-radius: 50%; background: var(--white); }
  .brand-name { font-weight: 700; font-size: 27px; letter-spacing: .5px; line-height: 1; }
  .brand-slogan { font-size: 12px; letter-spacing: 4.2px; margin-top: 7px; }
  .back-web { position: absolute; left: 208px; top: 196px; font-size: 12px; letter-spacing: 2.4px; }

  /* front */
  .company { position: absolute; left: 22px; top: 20px; }
  .company-name { color: var(--red); font-weight: 700; font-size: 25px; letter-spacing: .3px; line-height: 1; }
  .company-sub { display: flex; align-items: center; gap: 8px; margin-top: 5px; color: var(--navy); font-weight: 700; font-size: 14px; letter-spacing: 7px; }
  .company-sub::before, .company-sub::after { content: ""; flex: 1; height: 2px; background: var(--navy); }
  .person { position: absolute; left: 360px; top: 22px; }
  .person-name { color: var(--red); font-weight: 700; font-size: 18px; }
  .person-title { color: var(--navy); font-size: 12px; margin-top: 2px; }
  .contact { position: absolute; left: 300px; color: var(--white); font-size: 12px; display: flex; align-items: center; gap: 6px; }
  .contact-icon { width: 12px; height: 12px; }
  .address { position: absolute; left: 380px; top: 206px; color: var(--navy); font-size: 12.5px; line-height: 1.3; }
  .slogan { position: absolute; left: 72px; top: 196px; color: var(--white); font-weight: 700; font-size: 12px; letter-spacing: 2.5px; white-space: nowrap; }
  .social { position: absolute; left: 108px; top: 222px; display: flex; gap: 10px; }
  .social span { width: 18px; height: 18px; background: var(--white); border-radius: 2px; }
</style>
</head>
<body>
<main class="canvas">

  <section class="card card-back" aria-label="Card back">
    <div class="brand-lockup">
      <span class="brand-mark"></span>
      <div>
        <div class="brand-name">HARROWGATE PUMPS</div>
        <div class="brand-slogan">Rugged and Reliable</div>
      </div>
    </div>
    <div class="back-web">www.harrowgatesupply.com</div>
  </section>

  <section class="card card-front" aria-label="Card front">
    <svg class="shapes" width="540" height="309" viewBox="0 0 540 309">
      <line x1="190" y1="76" x2="540" y2="76" stroke="var(--navy)" stroke-width="1.2"/>
      <polygon points="225,86 540,86 540,110 205,110" fill="var(--red)"/>
      <polygon points="200,118 540,118 540,142 180,142" fill="var(--red)"/>
      <polygon points="175,150 540,150 540,174 155,174" fill="var(--red)"/>
      <polygon points="50,180 300,180 245,309 0,309 0,272" fill="var(--navy)"/>
      <polygon points="0,266 120,266 108,280 0,280" fill="var(--red)"/>
      <polygon points="0,288 100,288 88,302 0,302" fill="var(--red)"/>
    </svg>

    <div class="company">
      <div class="company-name">HARROWGATE SUPPLIES</div>
      <div class="company-sub">GROUP</div>
    </div>

    <div class="person">
      <div class="person-name">Daniel Reyes</div>
      <div class="person-title">Owner/President</div>
    </div>

    <div class="contact" style="top:91px">
      <svg class="contact-icon" viewBox="0 0 12 12"><circle cx="6" cy="6" r="6" fill="#fff"/><rect x="4" y="2.5" width="4" height="7" rx="1" fill="var(--red)"/></svg>
      555-014-2290
    </div>
    <div class="contact" style="top:123px">
      <svg class="contact-icon" viewBox="0 0 12 12"><circle cx="6" cy="6" r="6" fill="#fff"/><path d="M3 4.5c0-1 .6-1.5 1.2-1.5L5.2 5 4.6 5.6c.4.9 1 1.5 1.8 1.8L7 6.8 9 7.8c0 .6-.5 1.2-1.5 1.2C5 9 3 7 3 4.5z" fill="var(--red)"/></svg>
      555-014-7716
    </div>
    <div class="contact" style="top:155px">
      <svg class="contact-icon" viewBox="0 0 12 12"><circle cx="6" cy="6" r="6" fill="#fff"/><rect x="3" y="4" width="6" height="4.2" fill="var(--red)"/><path d="M3 4l3 2.3L9 4" stroke="#fff" stroke-width=".8" fill="none"/></svg>
      info@harrowgatesupply.com
    </div>

    <div class="address">PO Box 418<br>Ridge Road<br>Mesa, Arizona 85201</div>

    <div class="slogan">Rugged and Reliable</div>
    <div class="social" aria-label="Social links"><span></span><span></span><span></span></div>
  </section>

</main>
</body>
</html>
```